Family Ranch with a hobby vineyard needs 2 wine labels for our first harvest

Design 2 wine labels (front and back) with the Brindor Ranch logo.
Label 1:
Sauvignon Blanc
Alc. 12.5% by Vol.
Palos Verdes Peninsula - add as the region
Year 2022
Label 2:
Cabernet Sauvignon
Alc. 13.5% by Vol.
Year 2022
For the back label design:
GOVERNMENT WARNING: (1) According to the Surgeon General, women
should not drink alcoholic beverages during pregnancy because of the risk of
birth defects. (2) Consumption of alcoholic beverages impairs your ability to
drive a car or operate machinery, and may cause health problems.
Contains Sulfates.
750ML
I just received the bottles and have attached a picture.
Look and feel
Each slider illustrates characteristics of the customer's brand and the style your logo design should communicate.

```html
<!DOCTYPE html>
<html lang="en">
<head>
<meta charset="utf-8">
<title>Brindor Ranch – Back Label</title>
<link rel="stylesheet" href="https://fonts.googleapis.com/css2?family=Montserrat:wght@500;600&family=Open+Sans:wdth,wght@75..100,400&display=swap">
<style>
  :root {
    --label-tan: #c2b49a;
    --ink-brown: #5a4a3f;
  }
  html, body {
    margin: 0;
    padding: 0;
    overflow: hidden;
    background: var(--label-tan);
  }
  .back-label {
    position: relative;
    width: 1200px;
    height: 600px;
    background: var(--label-tan);
    color: var(--ink-brown);
    overflow: hidden;
  }
  .government-warning {
    position: absolute;
    left: 54px;
    top: 52px;
    margin: 0;
    font-family: "Open Sans", sans-serif;
    font-stretch: 78%;
    font-weight: 400;
    font-size: 32px;
    line-height: 48px;
    letter-spacing: -0.2px;
  }
  .government-warning .line {
    display: block;
    white-space: nowrap;
  }
  .sulfite-notice {
    position: absolute;
    left: 54px;
    top: 364px;
    margin: 0;
    font-family: "Montserrat", sans-serif;
    font-weight: 600;
    font-size: 24px;
    letter-spacing: 3.4px;
  }
  .volume {
    position: absolute;
    left: 54px;
    top: 492px;
    margin: 0;
    font-family: "Montserrat", sans-serif;
    font-weight: 600;
    font-size: 38px;
    letter-spacing: 5px;
  }
  .ranch-name {
    position: absolute;
    left: 930px;
    top: 330px;
    width: 234px;
    height: 240px;
    display: flex;
    flex-direction: column;
    align-items: center;
    justify-content: center;
    gap: 16px;
  }
  .ranch-name .dot {
    width: 22px;
    height: 22px;
    border-radius: 50%;
    background: var(--ink-brown);
  }
  .ranch-name .name {
    margin: 0;
    font-family: "Montserrat", sans-serif;
    font-weight: 600;
    font-size: 30px;
    line-height: 38px;
    letter-spacing: 2px;
    text-align: center;
    color: var(--ink-brown);
  }
</style>
</head>
<body>
  <main class="back-label">
    <p class="government-warning">
      <span class="line">GOVERNMENT WARNING: (1) According to the Surgeon General, women</span>
      <span class="line">should not drink alcoholic beverages during pregnancy because of the risk</span>
      <span class="line">of birth defects. (2) Consumption of alcoholic beverages impairs your ability</span>
      <span class="line">to drive a car or operate machinery, and may cause health problems.</span>
    </p>
    <p class="sulfite-notice">CONTAINS SULFITES</p>
    <p class="volume">750ML</p>
    <div class="ranch-name">
      <span class="dot" aria-hidden="true"></span>
      <p class="name">BRINDOR<br>RANCH</p>
    </div>
  </main>
</body>
</html>
```